CalmPath Nurses' Manifesto

Design a manifesto to inspire and motivate nurses to work at minimum standards of excellence in their nursing practice.

The manifesto will become a feature of our website, at conferences, workshops and retreats. It will also be featured on other marketing tools.

Primary Market:
Nurses and/or other healthcare professionals (specifically Doctors, Occupational Therapists, Psychologists and Social Workers).

However the manifesto is equally applicable to all nurses and healthcare professionals from new graduates to very experienced senior clinicians, administration officers,managers and healthcare executive personnel.

Mainly females and primarily 35 to 65 years old, which suggests people in this target age group have extensive experience, but have become jaded'.

The purpose of our business is to assist healthcare professionals, primarily nurses, to maintain their enthusiasm and excellence in service provision, for their benefit as well as the benefit of the clients.

I have attached:
File 1: Copy Samples and examples: which has the copy for the manifesto, examples that appeal to us and our 3 attempts.
File 2: Our colour Spec Sheet, HOWEVER the colours are not necessary limited to these colours. These colours are not in the logo that will be on the manifesto. The colours on the logo attached can/or also be used.
File 3: Prototype logo. The final logo will be available within 3 to 4 days.

Requirements
Must have
• Must use the copy as per the attached file.

It should be contemporary, eye catching and motivational.

Sample 1 on the attached file (File 3: copy, samples and examples_554207 saturday, 29 june 2013 06:24:3030) Is close to what we are looking for.
Should not have
• MUST BE EASY TO READ. Each line MUST be clearly defined from each other.

```html
<!DOCTYPE html>
<html lang="en">
<head>
<meta charset="utf-8">
<title>CalmPath Nurses Manifesto</title>
<link rel="stylesheet" href="https://fonts.googleapis.com/css2?family=Arimo:ital,wght@0,700;1,700&display=swap">
<style>
  :root {
    --mint-light: #e4f8f1;
    --mint: #aeeeda;
    --teal-wave: #5fd9b6;
    --lime: #8fdc1e;
    --lime-bright: #a6e82c;
    --green-text: #6cc42a;
    --green-pale: #9fd84a;
    --teal-dark: #1d5450;
    --teal-mid: #2aa9a0;
    --star: #9aa5a6;
    --white: #ffffff;
  }
  html, body {
    margin: 0;
    padding: 0;
    overflow: hidden;
    background: var(--white);
  }
  .poster {
    position: relative;
    width: 912px;
    height: 1200px;
    overflow: hidden;
    background:
      radial-gradient(ellipse 620px 520px at 0 120px, var(--mint) 0%, rgba(174,238,218,0.35) 45%, rgba(255,255,255,0) 80%),
      linear-gradient(90deg, var(--mint-light) 0%, var(--white) 30%, var(--white) 100%);
    font-family: "Arimo", Arial, sans-serif;
  }
  .hero-photo {
    position: absolute;
    top: 0;
    right: 0;
    width: 560px;
    height: 390px;
    background: linear-gradient(135deg, rgba(255,255,255,0) 0%, #e9d3c4 30%, #c79a80 55%, #8fd3d6 78%, #d9e4e6 100%);
    border-bottom-left-radius: 280px 200px;
  }
  .title {
    position: absolute;
    left: 78px;
    top: 172px;
    margin: 0;
    font-size: 76px;
    line-height: 78px;
    font-weight: 700;
    color: var(--lime);
    letter-spacing: -1px;
  }
  .manifesto {
    position: absolute;
    left: 120px;
    top: 365px;
    width: 740px;
    margin: 0;
    font-size: 18.5px;
    line-height: 29px;
    font-weight: 700;
    font-style: italic;
  }
  .manifesto .line { white-space: nowrap; }
  .star { color: var(--star); font-style: normal; font-size: 20px; }
  .dark { color: var(--teal-dark); }
  .green { color: var(--green-text); }
  .pale { color: var(--green-pale); }
  .teal { color: var(--teal-mid); }
  .lead { font-size: 23px; }
  .mid { font-size: 22px; }
  .big { font-size: 30px; }
  .closing { font-size: 30px; color: var(--teal-mid); margin-top: 28px; display: block; }
  .base-wave {
    position: absolute;
    left: 0;
    bottom: 0;
    width: 912px;
    height: 300px;
  }
  .brand {
    position: absolute;
    left: 548px;
    top: 978px;
    width: 190px;
    height: 190px;
    border-radius: 50%;
    background: var(--white);
    display: flex;
    align-items: center;
    justify-content: center;
    font-family: "Arimo", Arial, sans-serif;
    font-weight: 700;
    font-size: 28px;
    color: var(--green-text);
  }
</style>
</head>
<body>
<div class="poster">
  <div class="hero-photo" role="img" aria-label="Photo of a smiling nurse caring for an elderly woman"></div>

  <h1 class="title">Nurses<br>Manifesto</h1>

  <div class="manifesto">
    <div class="line"><span class="star">★</span> <span class="dark lead">Nurse with open hands, hearts and minds.</span></div>
    <div class="line">&nbsp;&nbsp;&nbsp;<span class="star">★</span> <span class="green">Look after yourself and value your health as much as you value the</span></div>
    <div class="line"><span class="green">health of others.</span> <span class="star">★</span> <span class="pale">Delight your clients and colleagues by exceeding</span></div>
    <div class="line"><span class="pale">their expectations.</span> <span class="star">★</span> <span class="teal mid">Deliver care skilfully.</span> <span class="star">★</span> <span class="dark">Respect the limits</span></div>
    <div class="line"><span class="dark">of other people’s knowledge and share your knowledge generously.</span></div>
    <div class="line"><span class="star">★</span> <span class="green">Support your colleagues and champion their purpose.</span> <span class="star">★</span> <span class="pale">Learn</span></div>
    <div class="line"><span class="pale">something new each day.</span> <span class="star">★</span> <span class="dark">Trust your knowledge and seek</span></div>
    <div class="line"><span class="dark">advice only from respected sources.</span> <span class="star">★</span> <span class="dark">Be a lifelong learner.</span> <span class="star">★</span></div>
    <div class="line"><span class="green">Celebrate, respect and value the diversity of your culture.</span> <span class="star">★</span></div>
    <div class="line"><span class="pale">Respond to distress with random acts of kindness.</span> <span class="star">★</span> <span class="green">Smile and</span></div>
    <div class="line"><span class="green">infect others with your happiness.</span> <span class="star">★</span> <span class="dark big">Have fun!</span> <span class="star">★</span> <span class="dark">Always</span></div>
    <div class="line"><span class="dark">do the right thing without exception.</span> <span class="star">★</span> <span class="green">You are unique, revel in your</span></div>
    <div class="line"><span class="green">individuality.</span> <span class="star">★</span> <span class="green">Don’t ever believe you’ve arrived, keep going.</span> <span class="star">★</span></div>
    <div class="line"><span class="dark">Always be solution focused.</span> <span class="star">★</span> <span class="green">Seek success, firstly from within.</span> <span class="star">★</span></div>
    <div class="line"><span class="green">Only follow exceptional leaders.</span> <span class="star">★</span> <span class="dark">If there’s no one left to follow, then</span></div>
    <div class="line"><span class="dark">lead!</span> <span class="star">★</span> <span class="green">Always lead with purpose, passion and commitment.</span> <span class="star">★</span></div>
    <div class="line"><span class="pale">Respond to complex situations innovatively, creatively and safely</span></div>
    <div class="line"><span class="pale">within the scope of your practice.</span> <span class="star">★</span> <span class="green">Adopt a ‘can do’ attitude to</span></div>
    <div class="line"><span class="green">anything that comes your way.</span> <span class="star">★</span> <span class="dark">Choose your thoughts wisely, they</span></div>
    <div class="line"><span class="dark">create your reality.</span></div>
    <div class="line"><span class="closing"><span class="star">★</span> Live your dream.</span></div>
  </div>

  <svg class="base-wave" viewBox="0 0 912 300" aria-hidden="true">
    <defs>
      <linearGradient id="waveFill" x1="0" y1="0" x2="0" y2="1">
        <stop offset="0" stop-color="#7fe3c6"/>
        <stop offset="1" stop-color="#52d4b0"/>
      </linearGradient>
    </defs>
    <path d="M0 90 C 200 180, 420 150, 560 80 C 700 10, 820 10, 912 40 L 912 300 L 0 300 Z" fill="url(#waveFill)"/>
    <path d="M0 140 C 220 210, 430 170, 570 100 C 710 30, 830 40, 912 70 L 912 300 L 0 300 Z" fill="#dff7ee"/>
    <path d="M0 140 C 220 210, 430 170, 570 100 C 710 30, 830 40, 912 70" fill="none" stroke="var(--lime-bright)" stroke-width="8"/>
  </svg>

  <div class="brand">CalmPath</div>
</div>
</body>
</html>
```